Home Page Design

We have a B2B home page design and need a consumer version. The look and feel can look similar but needs to be distinctly different so it in not to get confused. Essentially it should look like the same company with a different model. We will need a PSD w all layers organized and easy to understand. Attached is the logo, B2B comp, and a MS Word doc with a short description. In addition, I have attached a wire frame to be used as a site map. PLEASE DO NOT take that as the creative. I expect to see your creative based on the information provided.

Industry/Entity Type

Consumer

```html
<!DOCTYPE html>
<html lang="en">
<head>
<meta charset="utf-8">
<title>Orvella.com – Home</title>
<link rel="stylesheet" href="https://fonts.googleapis.com/css2?family=Cabin:wght@400;600;700&family=Cabin+Condensed:wght@500;600;700&family=Libre+Baskerville:ital@0;1&display=swap">
<style>
:root{
  --navy:#0a2a35;
  --ink:#1c2a3a;
  --blue:#1e6e98;
  --green:#2fae45;
  --green-dark:#23883a;
  --white:#ffffff;
  --grey:#e6e8ea;
  --line:#cfd4d8;
  --text:#333a40;
}
*{box-sizing:border-box;margin:0;padding:0}
html,body{width:1200px;height:3117px;overflow:hidden;background:var(--white)}
body{position:relative;font-family:"Cabin",sans-serif;color:var(--text)}
.abs{position:absolute}

/* hero */
.hero{left:0;top:0;width:1200px;height:755px;background:linear-gradient(160deg,#3f6b4a 0%,#2c6b66 35%,#0f6f7a 60%,#0a4c5c 100%);box-shadow:0 10px 18px rgba(0,0,0,.35)}
.nav{left:150px;top:18px;width:916px;height:72px;background:var(--white);box-shadow:0 3px 8px rgba(0,0,0,.3)}
.nav a{position:absolute;top:26px;font:700 17px "Cabin",sans-serif;color:var(--ink);text-decoration:none;text-transform:uppercase;white-space:nowrap}
.nav .l1{left:72px}.nav .l2{left:252px}.nav .l3{left:470px}.nav .l4{left:590px}
.follow{right:24px;top:0;width:150px;height:62px;background:var(--navy);color:var(--white);text-align:center;font:700 14px "Cabin",sans-serif;padding-top:6px}
.follow .dots{display:flex;justify-content:center;gap:8px;margin-top:8px}
.follow .dots span{width:22px;height:22px;border-radius:50%;background:#5c7a86}
.crest{left:415px;top:87px;width:375px;height:156px}
.brand{left:415px;top:138px;width:375px;text-align:center;font:600 30px "Cabin",sans-serif;color:var(--blue)}
.brand .dot{display:inline-block;width:24px;height:24px;border-radius:50%;background:var(--blue);vertical-align:-3px;margin-right:10px}
.hero-title{left:0;top:332px;width:1200px;text-align:center;font:400 56px "Cabin",sans-serif;color:var(--white);letter-spacing:1px}
.hero-sub{left:400px;top:408px;width:400px;text-align:center;font:400 18px/24px "Cabin",sans-serif;color:rgba(255,255,255,.85)}
.play{left:563px;top:494px;width:74px;height:74px}
.hero-cta{left:0;top:602px;width:1200px;text-align:center;color:var(--white);font:400 20px "Cabin",sans-serif}
.hero-cta small{display:block;font-size:14px;margin-top:6px}
.arrow{width:44px;height:82px;top:450px;display:flex;align-items:center;justify-content:center}
.arrow.left{left:0;background:#c9d0d3}.arrow.right{right:0;background:var(--green)}

/* about */
.about-title{left:0;top:810px;width:1200px;text-align:center;font:400 62px "Cabin",sans-serif;color:var(--ink)}
.about-text{left:225px;top:885px;width:750px;text-align:center;font:400 14px/19px "Libre Baskerville",serif;color:#444}
.rule{left:0;top:985px;width:1200px;height:2px;background:var(--grey)}

/* categories */
.tile{top:1041px;width:312px;height:206px}
.tile .photo{width:100%;height:100%}
.tile .label{position:absolute;left:0;top:92px;background:rgba(255,255,255,.85);padding:10px 18px;font:700 19px "Cabin Condensed",sans-serif;color:var(--ink)}

/* featured */
.featured{left:0;top:1306px;width:1200px;height:558px;background:var(--navy)}
.feat-title{left:112px;top:1356px;font:700 38px "Cabin Condensed",sans-serif;color:var(--white)}
.feat-title span{background:var(--blue);padding:0 8px}
.feat-rule{left:112px;top:1421px;width:988px;height:2px;background:#3d5963}
.card{top:1452px;width:296px;height:365px;background:var(--white);padding:14px}
.card .photo{width:268px;height:240px}
.card .name{margin-top:16px;font:400 17px "Libre Baskerville",serif;font-variant:small-caps;color:#333}
.card .name i{font-style:italic}
.card .row{display:flex;justify-content:space-between;align-items:center;margin-top:12px}
.card .price{font:400 30px "Cabin",sans-serif;color:#222}
.card .price sup{font-size:14px}
.card .btn{background:var(--blue);color:var(--white);font:600 16px "Cabin",sans-serif;padding:8px 10px;border-radius:3px}
.arrow.mid{top:1595px;height:82px}
.arrow.mid.left{background:#c9d0d3}.arrow.mid.right{background:var(--blue)}

/* tabs */
.tabs{left:193px;top:1930px;width:829px;height:56px;display:flex}
.tab{flex:1;border:2px solid var(--line);border-left:none;display:flex;align-items:center;justify-content:center;font:500 19px "Cabin Condensed",sans-serif;color:#444;background:var(--white)}
.tab:first-child{border:none;border-bottom:2px solid var(--line);font-weight:700;color:var(--ink);position:relative}
.tab:first-child::after{content:"";position:absolute;bottom:-12px;left:50%;margin-left:-10px;border:10px solid transparent;border-top-color:var(--ink);border-bottom:0}

/* products */
.prod{width:200px;text-align:center}
.prod .photo{width:200px;height:153px}
.prod .name{margin-top:18px;font:700 23px "Cabin Condensed",sans-serif;color:#111;text-transform:uppercase;white-space:nowrap}
.prod .price{font:600 21px "Cabin Condensed",sans-serif;color:#111}
.prod .price sup{font-size:11px}
.prod .add{display:inline-block;margin-top:10px;background:var(--green);color:var(--white);font:700 18px "Cabin Condensed",sans-serif;padding:5px 16px;border-radius:3px;box-shadow:0 3px 0 var(--green-dark)}

/* search footer */
.help{left:0;top:2752px;width:1200px;height:318px;background:var(--navy)}
.help-title{left:0;top:2790px;width:1200px;text-align:center;font:600 34px "Cabin",sans-serif;color:var(--white)}
.help-text{left:340px;top:2835px;width:520px;text-align:center;font:400 13px/16px "Libre Baskerville",serif;color:#c9d3d7}
.help-icon{width:60px;height:60px;border-radius:50%;background:var(--white);top:2912px;display:flex;align-items:center;justify-content:center}
.help-btn{top:2967px;width:335px;height:52px;border-radius:26px;background:var(--green);color:var(--navy);font:700 21px "Cabin Condensed",sans-serif;display:flex;align-items:center;justify-content:center;text-transform:uppercase}
.copyright{left:0;top:3070px;width:1200px;height:47px;display:flex;align-items:center;justify-content:center;font:700 13px "Cabin",sans-serif;color:#222;letter-spacing:1px}
</style>
</head>
<body>

<section class="hero abs" role="img" aria-label="Aerial photograph of a coastal golf resort with green fairways and turquoise sea"></section>

<nav class="nav abs">
  <a class="l1" href="#">Post your event</a>
  <a class="l2" href="#">Add auction items</a>
  <a class="l3" href="#">About</a>
  <a class="l4" href="#">Contact</a>
  <div class="follow abs">FOLLOW US<div class="dots"><span></span><span></span><span></span><span></span></div></div>
</nav>

<svg class="crest abs" viewBox="0 0 375 156" aria-hidden="true">
  <path d="M8 0H367V110L187.5 156L8 110Z" fill="#ffffff"/>
  <path d="M8 118L187.5 150L367 118" fill="none" stroke="#1e6e98" stroke-width="4"/>
</svg>
<div class="brand abs"><span class="dot"></span>Orvella.com</div>

<div class="arrow left abs"><svg width="16" height="26" viewBox="0 0 16 26"><path d="M13 2L3 13L13 24" fill="none" stroke="#fff" stroke-width="4"/></svg></div>
<div class="arrow right abs"><svg width="16" height="26" viewBox="0 0 16 26"><path d="M3 2L13 13L3 24" fill="none" stroke="#fff" stroke-width="4"/></svg></div>

<h1 class="hero-title abs">INCREDIBILE SERVICE</h1>
<p class="hero-sub abs">Luxury experiences, auction items and charity events all in one friendly place for you today.</p>
<svg class="play abs" viewBox="0 0 74 74" aria-label="Play video"><circle cx="37" cy="37" r="34" fill="none" stroke="#fff" stroke-width="4"/><path d="M29 22L53 37L29 52Z" fill="#fff"/></svg>
<p class="hero-cta abs">Start your new tour in life today!<small>No credit card required.</small></p>

<h2 class="about-title abs">LET'S TALK ABOUT US</h2>
<p class="about-text abs">We connect generous people with great causes through curated auctions, exclusive items and memorable events. Every bid helps a charity grow, and every purchase brings a little more joy to the community we serve together each day.</p>
<div class="rule abs"></div>

<div class="tile abs" style="left:112px"><div class="photo" role="img" aria-label="Golfer swinging on a green course" style="background:linear-gradient(160deg,#6f8c4a,#2f4a24)"></div><span class="label">GOLF WEDGES</span></div>
<div class="tile abs" style="left:452px"><div class="photo" role="img" aria-label="Row of luxury wristwatches in a store display" style="background:linear-gradient(180deg,#5d6b78,#1e2630)"></div><span class="label">LUXURIOUS WATCHES</span></div>
<div class="tile abs" style="left:792px"><div class="photo" role="img" aria-label="Yellow golf flag on a green under blue sky" style="background:linear-gradient(180deg,#3d8fd0 0%,#6aa8d8 55%,#4e8a2e 70%,#2e5e1e 100%)"></div><span class="label">PACKAGE SETS</span></div>

<section class="featured abs"></section>
<h2 class="feat-title abs">FEATURED <span>AUCTION ITEMS:</span></h2>
<div class="feat-rule abs"></div>

<div class="card abs" style="left:112px"><div class="photo" role="img" aria-label="Golf driver club head" style="background:radial-gradient(circle at 50% 50%,#9a9a9a,#2a2a2a 60%,#fff 61%)"></div><p class="name">Golf Wedeges <i>Exclusive</i></p><div class="row"><span class="price">45.99<sup>$</sup></span><span class="btn">Add to Cart</span></div></div>
<div class="card abs" style="left:458px"><div class="photo" role="img" aria-label="White golf shoe" style="background:radial-gradient(circle at 50% 55%,#d9d9d9,#9a9a9a 55%,#fff 62%)"></div><p class="name">Golf Wedeges <i>Exclusive</i></p><div class="row"><span class="price">75.99<sup>$</sup></span><span class="btn">Add to Cart</span></div></div>
<div class="card abs" style="left:804px"><div class="photo" role="img" aria-label="Golf bag with clubs" style="background:radial-gradient(circle at 50% 50%,#555,#141414 55%,#fff 62%)"></div><p class="name">Golf Wedeges <i>Exclusive</i></p><div class="row"><span class="price">145.99<sup>$</sup></span><span class="btn">Add to Cart</span></div></div>

<div class="arrow mid left abs"><svg width="16" height="26" viewBox="0 0 16 26"><path d="M13 2L3 13L13 24" fill="none" stroke="#fff" stroke-width="4"/></svg></div>
<div class="arrow mid right abs"><svg width="16" height="26" viewBox="0 0 16 26"><path d="M3 2L13 13L3 24" fill="none" stroke="#fff" stroke-width="4"/></svg></div>

<div class="tabs abs"><div class="tab">Best sellers</div><div class="tab">Comming Soon</div><div class="tab">Recently Added</div><div class="tab">Special Offers</div></div>

<div class="prod abs" style="left:112px;top:2054px"><div class="photo" role="img" aria-label="Golf ball on grass" style="background:linear-gradient(180deg,#3f6a2a,#7fae4a)"></div><p class="name">Golf Balls</p><p class="price">22.00<sup>$</sup></p><span class="add">ADD TO CART</span></div>
<div class="prod abs" style="left:377px;top:2054px"><div class="photo" role="img" aria-label="Set of golf wedges" style="background:linear-gradient(180deg,#4a4a4a,#1a1a1a)"></div><p class="name">Golf Wedeges</p><p class="price">122.00<sup>$</sup></p><span class="add">ADD TO CART</span></div>
<div class="prod abs" style="left:642px;top:2054px"><div class="photo" role="img" aria-label="Camera on set" style="background:linear-gradient(180deg,#6a6a6a,#202020)"></div><p class="name">On-Set Camera</p><p class="price">252.00<sup>$</sup></p><span class="add">ADD TO CART</span></div>
<div class="prod abs" style="left:904px;top:2054px"><div class="photo" role="img" aria-label="Luxury wristwatch" style="background:radial-gradient(circle,#b0b0b0,#111 60%)"></div><p class="name">Luxury Watch</p><p class="price">422.00<sup>$</sup></p><span class="add">ADD TO CART</span></div>

<div class="prod abs" style="left:112px;top:2397px"><div class="photo" role="img" aria-label="Golf ball on grass" style="background:linear-gradient(180deg,#3f6a2a,#7fae4a)"></div><p class="name">Golf Balls</p><p class="price">22.00<sup>$</sup></p><span class="add">ADD TO CART</span></div>
<div class="prod abs" style="left:377px;top:2397px"><div class="photo" role="img" aria-label="Set of golf wedges" style="background:linear-gradient(180deg,#4a4a4a,#1a1a1a)"></div><p class="name">Golf Wedeges</p><p class="price">122.00<sup>$</sup></p><span class="add">ADD TO CART</span></div>
<div class="prod abs" style="left:642px;top:2397px"><div class="photo" role="img" aria-label="Camera on set" style="background:linear-gradient(180deg,#6a6a6a,#202020)"></div><p class="name">On-Set Camera</p><p class="price">252.00<sup>$</sup></p><span class="add">ADD TO CART</span></div>
<div class="prod abs" style="left:904px;top:2397px"><div class="photo" role="img" aria-label="Luxury wristwatch" style="background:radial-gradient(circle,#b0b0b0,#111 60%)"></div><p class="name">Luxury Watch</p><p class="price">422.00<sup>$</sup></p><span class="add">ADD TO CART</span></div>

<section class="help abs"></section>
<h2 class="help-title abs">HELP YOU ON YOUR SEARCH</h2>
<p class="help-text abs">Find the perfect auction item or the next charity event near you. Browse by category, date or cause and start bidding in just a few simple steps today.</p>
<div class="help-icon abs" style="left:362px"><svg width="32" height="28" viewBox="0 0 32 28"><path d="M4 10H28V26H4Z" fill="#0a2a35"/><path d="M10 10V5H22V10" fill="none" stroke="#0a2a35" stroke-width="3"/></svg></div>
<div class="help-icon abs" style="left:795px"><svg width="30" height="30" viewBox="0 0 30 30"><rect x="3" y="5" width="24" height="22" fill="none" stroke="#0a2a35" stroke-width="3"/><path d="M3 11H27M9 2V8M21 2V8" stroke="#0a2a35" stroke-width="3"/></svg></div>
<div class="help-btn abs" style="left:225px">Search auction item</div>
<div class="help-btn abs" style="left:658px">Search for an event</div>

<footer class="copyright abs">© ORVELLA 2012-2015 ALL RIGHTS RESERVED</footer>

</body>
</html>
```